Mobile dental anesthesiologist needs a postcard to market to other doctors

This postcard is intended to inform dentists in the California Central Coast region that I am available to travel to their office to serve their patient's anesthesia needs. It is important to know that other anesthesiologists are usually booked for weeks in advance and are very costly. Our market niche is greater availability and lower cost. I would prefer a 2 sided oversized postcard. The attached images are DIY projects I've done recently...You can see why I'm reaching out to professionals.

Industry/Entity Type

Dental

```html
<!DOCTYPE html>
<html lang="en">
<head>
<meta charset="utf-8">
<title>Harbor Ridge Dental Anesthesia – Postcard</title>
<link href="https://fonts.googleapis.com/css2?family=Montserrat:wght@400;500;600;700&family=Lato:wght@400;700&display=swap" rel="stylesheet">
<style>
  :root {
    --orange: #ee6a24;
    --blue: #29a8e0;
    --green: #8cc63f;
    --green-dark: #5a9a34;
    --charcoal: #2b2d2f;
    --ink: #222222;
    --body: #333333;
    --white: #ffffff;
    --stage: #e9e6e2;
    --stamp: #b5b5b5;
  }
  * { margin: 0; padding: 0; box-sizing: border-box; }
  html, body { width: 907px; height: 1200px; overflow: hidden; }
  body { background: var(--stage); position: relative; font-family: "Lato", sans-serif; }

  .card {
    position: absolute; left: 100px; width: 710px; height: 510px;
    background: var(--white); overflow: hidden;
    box-shadow: 0 4px 12px rgba(0,0,0,.25);
  }
  .card--front { top: 50px; }
  .card--back { top: 604px; height: 512px; }
  .card svg.shapes { position: absolute; inset: 0; }

  /* front */
  .front__headline { position: absolute; right: 32px; top: 50px; text-align: right; font-family: "Montserrat", sans-serif; }
  .front__headline h1 { color: var(--orange); font-size: 27px; font-weight: 700; letter-spacing: .2px; line-height: 1; }
  .front__headline p { color: var(--ink); font-size: 20px; font-weight: 400; margin-top: 7px; }
  .front__banner { position: absolute; right: 38px; top: 170px; text-align: right; font-family: "Montserrat", sans-serif; font-size: 25px; line-height: 34px; }
  .front__banner strong { color: var(--white); font-weight: 700; display: block; }
  .front__banner span { color: var(--ink); font-weight: 400; }
  .front__copy {
    position: absolute; left: 322px; top: 309px; width: 359px;
    font-size: 11px; line-height: 15px; color: var(--body); text-align: justify; text-align-last: right;
  }
  .brand { position: absolute; left: 42px; top: 392px; font-family: "Montserrat", sans-serif; font-weight: 500; color: var(--green-dark); font-size: 20px; line-height: 24px; display: flex; align-items: center; gap: 8px; }
  .brand__dot { width: 12px; height: 12px; border-radius: 50%; background: var(--orange); flex: none; }
  .front__bar {
    position: absolute; left: 0; right: 0; bottom: 0; height: 58px;
    background: var(--charcoal); border-top: 3px solid var(--blue);
    display: flex; justify-content: space-between; align-items: center; padding: 0 38px 4px 42px;
    font-family: "Lato", sans-serif; font-size: 16px;
  }
  .label { color: var(--green); font-weight: 400; }
  .value { color: var(--white); font-weight: 700; }

  /* back */
  .back__pitch { position: absolute; left: 55px; top: 213px; font-family: "Montserrat", sans-serif; color: var(--ink); }
  .back__pitch .kicker { color: var(--orange); font-weight: 700; font-size: 16.5px; letter-spacing: .3px; }
  .back__pitch .lead { font-size: 27px; font-weight: 500; line-height: 32px; letter-spacing: .2px; }
  .back__pitch .tail { font-size: 18px; font-weight: 400; }
  .benefits { position: absolute; list-style: none; font-size: 13.5px; color: var(--ink); line-height: 19px; }
  .benefits li { padding-left: 14px; position: relative; }
  .benefits li::before {
    content: ""; position: absolute; left: 1px; top: 6px; width: 5px; height: 5px;
    border-right: 2px solid var(--blue); border-top: 2px solid var(--blue); transform: rotate(45deg);
  }
  .benefits--left { left: 45px; top: 300px; }
  .benefits--right { left: 222px; top: 304px; width: 160px; }
  .back__contact { position: absolute; left: 46px; top: 414px; font-family: "Lato", sans-serif; font-size: 24px; line-height: 31px; }
  .back__contact .value { font-weight: 400; }
  .back__contact .email { font-size: 21px; }
  .stamp { position: absolute; left: 614px; top: 24px; width: 71px; height: 80px; background: var(--stamp); }
</style>
</head>
<body>

<section class="card card--front" aria-label="Postcard front">
  <svg class="shapes" viewBox="0 0 710 510" width="710" height="510">
    <defs>
      <linearGradient id="photoFront" x1="0" y1="0" x2="1" y2="1">
        <stop offset="0" stop-color="#f1ebe0"/>
        <stop offset=".55" stop-color="#e9e2cf"/>
        <stop offset="1" stop-color="#cfc4ad"/>
      </linearGradient>
      <linearGradient id="swoosh" x1="0" y1="0" x2="1" y2="0">
        <stop offset="0" stop-color="#b6d84a"/>
        <stop offset="1" stop-color="#5a9a34"/>
      </linearGradient>
    </defs>
    <path d="M0 330 C90 368 180 362 230 345 L230 365 C160 380 70 372 0 352Z" fill="var(--green)"/>
    <path role="img" aria-label="Photo: a dental clinician in a white coat greeting a smiling senior patient" d="M0 0 H300 C362 90 352 252 230 332 C170 366 80 356 0 322Z" fill="url(#photoFront)"/>
    <path d="M305 0 C372 92 360 262 236 340 C176 374 90 366 0 332" fill="none" stroke="var(--orange)" stroke-width="7"/>
    <path d="M328 0 C398 104 372 278 246 350" fill="none" stroke="var(--blue)" stroke-width="4"/>
    <path d="M352 256 C470 246 600 250 710 266" fill="none" stroke="#d2d2d2" stroke-width="5"/>
    <path d="M345 250 C440 172 580 136 710 130 V260 C590 244 460 240 345 250Z" fill="url(#swoosh)"/>
  </svg>

  <div class="front__headline">
    <h1>DENTAL ANESTHESIA</h1>
    <p>Opening Doors to Treatment</p>
  </div>
  <div class="front__banner">
    <strong>Harbor Ridge</strong>
    <span>Dental Anesthesia</span>
  </div>
  <p class="front__copy">Some patients either require or would greatly benefit from treatment under anesthesia. You have seen them in your practice: the very young, those with special needs, the extremely anxious, and those undergoing invasive procedures. Put your patients and their families at ease by offering safe and effective anesthesia. Dr. Owen Hale is a Dentist Anesthesiologist with experience in treating patients with a wide spectrum of ages and conditions. Call to schedule a discussion of how anesthesia may benefit your practice</p>
  <div class="brand"><span class="brand__dot"></span><span>Harbor Ridge<br>Dental Anesthesia</span></div>
  <div class="front__bar">
    <p><span class="label">Call-</span>&nbsp;&nbsp; <span class="value">555.014.2783</span></p>
    <p><span class="label">Email-</span> <span class="value">owenhale@example.com</span></p>
  </div>
</section>

<section class="card card--back" aria-label="Postcard back">
  <svg class="shapes" viewBox="0 0 710 512" width="710" height="512">
    <defs>
      <linearGradient id="photoBack" x1="0" y1="0" x2="0" y2="1">
        <stop offset="0" stop-color="#c9dcea"/>
        <stop offset=".6" stop-color="#e3edf4"/>
        <stop offset="1" stop-color="#ffffff"/>
      </linearGradient>
    </defs>
    <path role="img" aria-label="Photo: clinician holding a stethoscope with sketched medical icons" d="M0 0 H362 C390 60 402 130 400 200 H0Z" fill="url(#photoBack)"/>
    <path d="M0 370 C120 370 230 396 380 378 C368 430 350 472 330 512 H0Z" fill="var(--charcoal)"/>
    <path d="M0 366 C120 366 230 392 380 374" fill="none" stroke="var(--orange)" stroke-width="5"/>
    <path d="M362 0 C418 120 432 330 330 512" fill="none" stroke="var(--green)" stroke-width="9"/>
    <path d="M384 0 C442 130 452 340 350 512" fill="none" stroke="var(--orange)" stroke-width="6"/>
  </svg>

  <div class="back__pitch">
    <p class="kicker">ANESTHESIA CAN OPEN DOORS</p>
    <p class="lead">TO TREATMENT THAT</p>
    <p class="tail">would otherwise never happen</p>
  </div>
  <ul class="benefits benefits--left">
    <li>Your Patients</li>
    <li>Your Office</li>
    <li>Safe and Effective</li>
  </ul>
  <ul class="benefits benefits--right">
    <li>No Anesthesia Billing Headaches—leave that to us!</li>
  </ul>
  <div class="back__contact">
    <p><span class="label">Call-</span> <span class="value">555.014.2783</span></p>
    <p class="email"><span class="label">Email-</span> <span class="value">owenhale@example.com</span></p>
  </div>
  <div class="stamp" aria-label="Postage area"></div>
</section>

</body>
</html>
```